Business Cards for GPS Technology Business - Logo Supplied

Varel Systems Ltd. requires a business card design. Varel is a startup GPS vehicle fleet tracking vendor. Our hardware/software helps business fleets be more productive and reduce operating costs. Our systems utilize a mix of GPS satellite, cell network and web technologies.
We would like to see a double sided original design utilizing our existing logo. Please use whatever colors will work with the blue logo.
As a business, we want to project the image of friendly and approachable lifetime business partners and advisors to our customers - “someone you can trust”. Words customers will use to describe us will include: knowledgeable, supportive, trustworthy and honest.
We will also require Vidplex, Chirpa, Frendly and Lumo+ backgrounds. Winner will be first in line to quote for this work (separate project).
Target Market(s)
Target audience are working owners and managers of vehicle fleets. Usually male, age 30 to 60. Often have a trades background.
Industry/Entity Type
Business
Font styles to use
Requirements
Must have
- Please use the following dummy data for the design:
name: Tim Varel
title: Director
address: 2381 Calden Lane
city: Larkvale, ON
postal code: K7P 2W4
cell phone number: 555-214-7390
business number: 555-318-4602
toll free number: 1-800-555-0193
web site address: www.varel-example.com
tagline: GPS Fleet Tracking Specialists
Nice to have
- Abstract imagery relating to GPS tracking / fleet vehicles / technology
Should not have
- Do not use serif fonts.

```html
<!DOCTYPE html>
<html lang="en">
<head>
<meta charset="utf-8">
<title>Varel Systems – Business Cards</title>
<link rel="stylesheet" href="https://fonts.googleapis.com/css2?family=Open+Sans:wght@400;600;800&display=swap">
<style>
  :root {
    --brand-blue: #1f6db8;
    --card-white: #ffffff;
    --card-grey: #e9ecef;
    --text-dark: #4a4f55;
    --page-bg: #d9dcdf;
  }
  * { margin: 0; padding: 0; box-sizing: border-box; }
  html, body { width: 1200px; height: 939px; overflow: hidden; }
  body {
    background: var(--page-bg);
    font-family: "Open Sans", Arial, sans-serif;
    position: relative;
  }
  .card {
    position: absolute;
    width: 700px;
    height: 400px;
    background: linear-gradient(135deg, var(--card-white) 55%, var(--card-grey) 100%);
    box-shadow: 0 10px 28px rgba(0,0,0,0.25);
    overflow: hidden;
  }
  .card-shapes { position: absolute; inset: 0; width: 100%; height: 100%; }
  .card--front { left: 70px; top: 60px; }
  .card--back { left: 430px; top: 480px; }

  .wordmark {
    position: absolute;
    font-weight: 800;
    letter-spacing: 2px;
    line-height: 1;
    white-space: nowrap;
  }
  .card--front .wordmark {
    left: 56px; top: 236px;
    font-size: 84px;
    color: var(--card-white);
  }
  .tagline {
    position: absolute;
    font-weight: 600;
    letter-spacing: 1.5px;
    text-transform: uppercase;
    color: var(--card-white);
    white-space: nowrap;
  }
  .card--front .tagline { left: 60px; top: 334px; font-size: 16px; }

  .contact-name {
    position: absolute;
    right: 40px; top: 38px;
    font-size: 26px;
    color: var(--text-dark);
  }
  .contact-name strong { font-weight: 600; }
  .contact-name .divider { color: var(--brand-blue); margin: 0 6px; }
  .card--back .wordmark {
    right: 40px; top: 92px;
    font-size: 104px;
    color: var(--brand-blue);
  }
  .contact-list {
    position: absolute;
    right: 40px; top: 218px;
    width: 560px;
    font-size: 15px;
    color: var(--text-dark);
  }
  .contact-row {
    display: flex;
    justify-content: flex-end;
    gap: 18px;
    margin-bottom: 12px;
  }
  .contact-item { display: flex; align-items: center; gap: 6px; white-space: nowrap; }
  .contact-icon { width: 16px; height: 16px; flex: none; }
  .card--back .tagline { right: 40px; top: 345px; font-size: 18px; }
</style>
</head>
<body>

<section class="card card--front" aria-label="Business card front">
  <svg class="card-shapes" viewBox="0 0 700 400" aria-hidden="true">
    <path fill="var(--brand-blue)" d="M0,150 H390 C450,150 468,112 478,62 C488,20 512,0 560,0 H700 V40 C640,230 480,350 250,400 H0 Z"/>
  </svg>
  <div class="wordmark">VAREL</div>
  <div class="tagline">GPS Fleet Tracking Specialists</div>
</section>

<section class="card card--back" aria-label="Business card back">
  <svg class="card-shapes" viewBox="0 0 700 400" aria-hidden="true">
    <path fill="var(--brand-blue)" d="M0,0 H250 C130,80 60,220 95,400 H0 Z"/>
    <path fill="var(--brand-blue)" d="M290,400 C318,332 372,305 460,305 H700 V400 Z"/>
  </svg>
  <div class="contact-name"><strong>Tim Varel</strong><span class="divider">|</span>Director</div>
  <div class="wordmark">VAREL</div>
  <div class="contact-list">
    <div class="contact-row">
      <span class="contact-item">
        <svg class="contact-icon" viewBox="0 0 16 16" aria-hidden="true"><circle cx="8" cy="8" r="8" fill="var(--brand-blue)"/><path d="M5 4h2l1 2-1 1c.5 1 1 1.5 2 2l1-1 2 1v2c-4 0-7-3-7-7z" fill="#fff"/></svg>
        555-318-4602
      </span>
      <span class="contact-item">
        <svg class="contact-icon" viewBox="0 0 16 16" aria-hidden="true"><circle cx="8" cy="8" r="8" fill="var(--brand-blue)"/><rect x="5.5" y="3.5" width="5" height="9" rx="1" fill="#fff"/></svg>
        555-214-7390
      </span>
      <span class="contact-item">
        <svg class="contact-icon" viewBox="0 0 16 16" aria-hidden="true"><circle cx="8" cy="8" r="8" fill="var(--brand-blue)"/><path d="M4 6c2-2 6-2 8 0l-1 1.5-1.5-.5V6H6.5v1L5 7.5z M5 9h6v3H5z" fill="#fff"/></svg>
        1-800-555-0193
      </span>
    </div>
    <div class="contact-row">
      <span class="contact-item">
        <svg class="contact-icon" viewBox="0 0 16 16" aria-hidden="true"><circle cx="8" cy="8" r="8" fill="var(--brand-blue)"/><path d="M8 3a3 3 0 0 1 3 3c0 2.5-3 6-3 6S5 8.5 5 6a3 3 0 0 1 3-3z" fill="#fff"/><circle cx="8" cy="6" r="1" fill="var(--brand-blue)"/></svg>
        2381 Calden Lane, Larkvale, ON, K7P 2W4
      </span>
      <span class="contact-item">
        <svg class="contact-icon" viewBox="0 0 16 16" aria-hidden="true"><circle cx="8" cy="8" r="8" fill="var(--brand-blue)"/><circle cx="8" cy="8" r="4.5" fill="none" stroke="#fff" stroke-width="1"/><path d="M3.5 8h9M8 3.5c-2 2.5-2 6.5 0 9M8 3.5c2 2.5 2 6.5 0 9" fill="none" stroke="#fff" stroke-width="1"/></svg>
        www.varel-example.com
      </span>
    </div>
  </div>
  <div class="tagline">GPS Fleet Tracking Specialists</div>
</section>

</body>
</html>
```